Web design for a dental and eye clinic

We need a web design for a dental and eye clinic ( with medical laboratory services) with two branches in Lagos Nigeria. The ultimate aim is to attract more patronage. The design should have links to social media and should have provision for appointments and enquiries. Blue should be part of the colours

Name of facility. VORANTACARE Added Saturday, May 27, 2017

Target Market(s)

Lagos. Nigeria

Industry/Entity Type

Health Care

Number of Pages Required

3 page

Font styles to use
Sans Serif

Colors
85cae6
cadf82

Requirements
Must have
• a projection of the professioal services rendered
Nice to have
• portal for enquiries and appointments
• Link to our facebook, twitter and instagram

```html
<!DOCTYPE html>
<html lang="en">
<head>
<meta charset="utf-8">
<title>Vorantacare – Dental, Eye &amp; Laboratory Services</title>
<link href="https://fonts.googleapis.com/css2?family=Raleway:wght@400;500;600;700&family=Open+Sans:wght@400;600;700&display=swap" rel="stylesheet">
<style>
:root{
  --blue:#1e9ad6;
  --blue-dark:#1578ad;
  --sky:#85cae6;
  --lime:#cadf82;
  --ink:#2b2f33;
  --text:#6a6f75;
  --line:#e4e6e8;
  --tab:#efefef;
  --footer:#2a2e33;
  --footer-deep:#1f2226;
  --white:#ffffff;
}
*{box-sizing:border-box;margin:0;padding:0}
html,body{width:1200px;height:3772px;overflow:hidden}
body{font-family:"Open Sans",Arial,sans-serif;color:var(--text);background:var(--white);font-size:13px;line-height:1.65;position:relative}
h1,h2,h3,h4{font-family:"Raleway",Arial,sans-serif;color:var(--ink);font-weight:600}
.abs{position:absolute}

/* top bar */
.topbar{position:absolute;top:0;left:0;width:1200px;height:40px;background:var(--blue-dark);color:var(--white);font-size:12px;display:flex;align-items:center;padding:0 40px;justify-content:space-between}
.social{display:flex;gap:12px}
.social span{width:16px;height:16px;border-radius:50%;background:rgba(255,255,255,.85);display:block}
.contacts{display:flex;gap:32px}
.contacts span{display:flex;align-items:center;gap:6px}

/* header */
.header{position:absolute;top:40px;left:0;width:1200px;height:128px;display:flex;align-items:center;justify-content:space-between;padding:0 40px;border-bottom:1px solid var(--line)}
.brand{display:flex;align-items:center;gap:12px;font-family:"Raleway",sans-serif;font-weight:700;font-size:30px;color:var(--blue);letter-spacing:1px}
.brand i{width:22px;height:22px;border-radius:50%;background:var(--blue);display:block}
.nav{display:flex;height:128px}
.nav a{display:flex;align-items:center;padding:0 18px;color:var(--ink);text-decoration:none;font-size:14px;font-family:"Raleway",sans-serif;font-weight:500}
.nav a.active{border-top:3px solid var(--blue);color:var(--blue);background:#f6f9fb}

/* hero */
.hero{position:absolute;top:168px;left:0;width:1200px;height:400px;background:linear-gradient(90deg,#f4f6f7 0%,#eef1f2 35%,#d9c2a8 60%,#8c5a3c 100%)}
.hero-photo{position:absolute;right:0;top:0;width:700px;height:400px;background:radial-gradient(ellipse at 55% 45%,#b07a55 0%,#7c4a30 45%,rgba(180,130,95,0) 80%)}
.hero-copy{position:absolute;left:40px;top:90px;width:360px}
.hero-copy h1{font-size:40px;color:var(--blue);font-weight:600;margin-bottom:10px}
.hero-copy p{font-size:14px;color:var(--ink);margin-bottom:26px}
.btn-dark{display:inline-block;background:#1d1f22;color:var(--white);padding:10px 22px;border-radius:20px;font-size:12px;font-weight:600}

/* feature cards */
.card{position:absolute;width:330px;height:162px;background:var(--white);box-shadow:0 4px 16px rgba(0,0,0,.08);padding:24px 22px 0 96px}
.card .ico{position:absolute;left:24px;top:26px;width:56px;height:56px;border-radius:50%;border:2px solid var(--blue);display:flex;align-items:center;justify-content:center}
.card h3{font-size:22px;font-weight:500;margin-bottom:4px}
.card p{font-size:12px;line-height:1.5}
.card .more{position:absolute;left:96px;bottom:14px;font-size:12px;color:var(--ink);font-weight:600;display:flex;align-items:center;gap:6px}
.card.on{background:var(--blue);color:var(--white);height:184px;top:530px}
.card.on h3,.card.on .more{color:var(--white)}
.card.on .ico{border-color:var(--white)}

/* section title */
.stitle{position:absolute;font-size:26px;font-weight:600;color:var(--ink);padding-bottom:10px;line-height:1.3}
.stitle:after{content:"";position:absolute;left:0;bottom:0;width:50px;height:3px;background:var(--blue)}
.divider{position:absolute;left:0;width:1200px;height:1px;background:var(--line)}

/* about */
.about-text{position:absolute;left:40px;top:800px;width:620px}
.hours{position:absolute;left:700px;top:760px;width:460px;border-collapse:collapse;font-size:14px}
.hours td{padding:12px 18px;border-bottom:1px solid var(--line);color:var(--ink)}
.hours tr{background:#f7f7f7}
.hours tr:nth-child(2){background:var(--white)}
.hours td:last-child{text-align:right}
.hours tr.today td{color:var(--blue)}

/* tabs */
.tabs{position:absolute;left:40px;width:360px;list-style:none}
.tabs li{background:var(--tab);margin-bottom:4px;padding:10px 18px;font-size:13px;font-weight:600;color:var(--ink);font-family:"Raleway",sans-serif;letter-spacing:.5px}
.tabs li.active{background:var(--blue);color:var(--white)}
.pane{position:absolute;left:440px;width:720px}
.pane h3{font-size:22px;color:var(--blue);font-weight:500;margin-bottom:8px}
.pane p{font-size:13px}
.photo{position:absolute}
.caption{position:absolute;font-family:"Raleway",sans-serif;font-weight:700;font-size:16px;color:var(--ink);text-align:center}

/* appointment */
.appt{position:absolute;top:2390px;left:0;width:1200px;height:440px;background:linear-gradient(100deg,#c9d2d6 0%,#a9b7bd 30%,#7e8f97 60%,#5c6c74 100%)}
.form-box{position:absolute;left:670px;top:30px;width:470px;height:380px;background:rgba(30,36,42,.82);padding:28px 30px;color:var(--white)}
.form-box h2{color:var(--white);font-size:28px;font-weight:500;text-align:center}
.form-box .sub{text-align:center;font-size:13px;margin-bottom:20px;color:#d0d6da}
.fields{display:grid;grid-template-columns:1fr 1fr;gap:12px}
.field{height:38px;background:var(--white);color:#8a8f94;font-size:12px;padding:0 12px;display:flex;align-items:center;justify-content:space-between}
.btn-blue{background:var(--blue);color:var(--white);height:38px;display:flex;align-items:center;justify-content:center;font-size:12px;font-weight:700;letter-spacing:.5px}

/* blog */
.blog-title{position:absolute;top:2880px;left:0;width:1200px;text-align:center;font-size:30px}
.blog-title:after{content:"";display:block;width:50px;height:3px;background:var(--blue);margin:10px auto 0}
.post h4{font-size:15px;margin-bottom:2px}
.post .meta{font-size:11px;color:var(--blue);margin-bottom:8px}
.post p{font-size:12px;line-height:1.55}
.post{position:absolute}

/* footer */
.footer{position:absolute;top:3280px;left:0;width:1200px;height:460px;background:var(--footer);color:#b8bec4;padding:50px 40px}
.footer h4{color:var(--white);font-size:18px;font-weight:600;margin-bottom:22px;letter-spacing:.5px}
.fcol{position:absolute;top:50px}
.fcol .row{display:flex;gap:10px;align-items:flex-start;margin-bottom:14px;font-size:13px}
.links{list-style:none}
.links li{font-size:13px;margin-bottom:8px}
.links li:first-child{color:var(--blue)}
.finput{width:320px;height:34px;border:1px solid #4a5057;background:transparent;margin-bottom:10px;padding:0 10px;font-size:12px;display:flex;align-items:center;color:#8a9096}
.finput.tall{height:70px;align-items:flex-start;padding-top:8px}
.fbtn{display:inline-block;background:var(--white);color:var(--ink);font-size:12px;font-weight:700;padding:7px 16px}
.bottombar{position:absolute;top:3740px;left:0;width:1200px;height:32px;background:var(--footer-deep);color:#8c9298;font-size:11px;display:flex;align-items:center;justify-content:space-between;padding:0 40px}
</style>
</head>
<body>

<div class="topbar">
  <div class="social"><span></span><span></span><span></span></div>
  <div class="contacts">
    <span><svg width="12" height="12" viewBox="0 0 24 24"><path fill="#fff" d="M12 2a7 7 0 0 0-7 7c0 5 7 13 7 13s7-8 7-13a7 7 0 0 0-7-7zm0 9.5a2.5 2.5 0 1 1 0-5 2.5 2.5 0 0 1 0 5z"/></svg>21 Harbour Crest Road, Lekki, Lagos</span>
    <span><svg width="12" height="12" viewBox="0 0 24 24"><path fill="#fff" d="M2 5h20v14H2z M2 5l10 8 10-8" stroke="#1578ad" stroke-width="1.5"/></svg>hello@vorantacare.com</span>
    <span><svg width="12" height="12" viewBox="0 0 24 24"><path fill="#fff" d="M6.6 10.8a15 15 0 0 0 6.6 6.6l2.2-2.2c.3-.3.7-.4 1-.2 1.1.4 2.3.6 3.6.6.6 0 1 .4 1 1V20c0 .6-.4 1-1 1A17 17 0 0 1 3 4c0-.6.4-1 1-1h3.5c.6 0 1 .4 1 1 0 1.3.2 2.5.6 3.6.1.3 0 .7-.2 1z"/></svg>+234 800 555 0142</span>
  </div>
</div>

<header class="header">
  <div class="brand"><i></i>VORANTACARE</div>
  <nav class="nav">
    <a class="active">Home</a><a>Dental Services</a><a>Eye Services</a><a>Appointment</a><a>Blog</a><a>Careers</a><a>Contact Us</a><a>Staff</a>
  </nav>
</header>

<section class="hero">
  <div class="hero-photo" role="img" aria-label="Photo of a smiling family of four gathered together"></div>
  <div class="hero-copy">
    <h1>Vorantacare</h1>
    <p>Vorantacare is a state of the art dental and eye clinic that takes care of everything mouth &amp; eyes in Lagos, Nigeria.</p>
    <span class="btn-dark">Make an Appointment</span>
  </div>
</section>

<div class="card" style="left:110px;top:552px">
  <div class="ico"><svg width="28" height="28" viewBox="0 0 24 24"><path fill="none" stroke="#1e9ad6" stroke-width="1.6" d="M7 3c-3 0-4 3-3 6 1 4 1 12 3 12 2 0 2-6 5-6s3 6 5 6c2 0 2-8 3-12 1-3 0-6-3-6-2 0-3 1-5 1S9 3 7 3z"/></svg></div>
  <h3>Dental care</h3>
  <p>Dental implants is a very popular dental procedure in today's practice.</p>
  <span class="more">&#8250; Read More</span>
</div>
<div class="card on" style="left:440px">
  <div class="ico"><svg width="30" height="30" viewBox="0 0 24 24"><path fill="none" stroke="#fff" stroke-width="1.6" d="M2 12s4-6 10-6 10 6 10 6-4 6-10 6S2 12 2 12z"/><circle cx="12" cy="12" r="3" fill="none" stroke="#fff" stroke-width="1.6"/></svg></div>
  <h3>Eye care</h3>
  <p>During a comprehensive eye exam with us, we will do more than check your vision.</p>
  <span class="more">&#8250; Read More</span>
</div>
<div class="card" style="left:770px;top:552px">
  <div class="ico"><svg width="28" height="28" viewBox="0 0 24 24"><path fill="none" stroke="#1e9ad6" stroke-width="1.6" d="M9 3h6M10 3v6L4 20h16L14 9V3"/></svg></div>
  <h3>Laboratory services</h3>
  <p>Contrary to popular belief, Lorem Ipsum is not simply random text.</p>
  <span class="more">&#8250; Read More</span>
</div>

<h2 class="stitle" style="left:40px;top:745px">About Vorantacare</h2>
<p class="about-text">There are many variations of passages of text available, but the majority have suffered alteration in some form, by injected humour, or randomised words which don't look even slightly believable. If you are going to use a passage of text, you need to be sure there isn't anything embarrassing hidden in the middle of text.</p>
<table class="hours">
  <tr><td>Monday – Friday</td><td>08 Am – 10 Pm</td></tr>
  <tr><td>Saturday</td><td>08 Am – 12 Pm</td></tr>
  <tr class="today"><td>Sunday</td><td>08 Am – 12 Pm</td></tr>
</table>

<div class="divider" style="top:950px"></div>

<h2 class="stitle" style="left:40px;top:1000px">Dental Services</h2>
<ul class="tabs" style="top:1064px">
  <li class="active">DENTAL IMPLANTS</li><li>ROOT CANAL TREATMENT</li><li>INVISALIGN</li><li>FIXED BRACES</li>
</ul>
<div class="pane" style="top:1000px">
  <h3>Dental Implants</h3>
  <p>Dental implants is a very popular dental procedure in today's dental center, for a number of reasons. It's one way of replacing a missing tooth. A post is placed in the jaw bone to support a replacement tooth. The core lies the root of a natural tooth. Implants can also be used to support fixed bridges or dentures. The implant offers the patient the opportunity to regain normal function of the teeth.</p>
</div>
<div class="photo" role="img" aria-label="Close-up of teeth before dental implant treatment" style="left:440px;top:1160px;width:320px;height:190px;background:linear-gradient(135deg,#c98a86 0%,#e8d6cc 55%,#b56f6c 100%)"></div>
<div class="photo" role="img" aria-label="Close-up of teeth after dental implant treatment" style="left:790px;top:1160px;width:320px;height:190px;background:linear-gradient(135deg,#cf9591 0%,#f3ece6 55%,#bd7a76 100%)"></div>
<div class="caption" style="left:440px;top:1360px;width:320px">BEFORE</div>
<div class="caption" style="left:790px;top:1360px;width:320px">AFTER</div>

<div class="divider" style="top:1440px"></div>

<h2 class="stitle" style="left:40px;top:1490px">Eye Services</h2>
<ul class="tabs" style="top:1554px">
  <li class="active">COMPREHENSIVE EYE CARE</li><li>SURGICAL CONSULTATION</li><li>GLAUCOMA SURGERY</li><li>OPTICAL SERVICES</li>
</ul>
<div class="pane" style="top:1500px">
  <h3>Comprehensive Eye Care</h3>
  <p>Routine eye exams are important regardless of your age or your physical health. During a comprehensive eye exam with us, we will do more than just determine your prescription for eyeglasses or contact lenses. We will also check your eyes for common eye diseases, assess how your eyes work together as a team and evaluate your eyes as an indicator of your overall health. These eye examinations are an important part of health maintenance for everyone. Adults should have their eyes tested to keep their prescriptions current and to check for early signs of eye disease. Children's eye exams are important to ensure normal vision development and academic achievement.</p>
</div>
<div class="photo" role="img" aria-label="Patient having an eye examination with an optometry instrument" style="left:440px;top:1730px;width:400px;height:230px;background:linear-gradient(120deg,#e9ecee,#c7cdd1 50%,#8e969b)"></div>
<div class="photo" role="img" aria-label="Close-up of an eye test with a slit lamp" style="left:860px;top:1730px;width:300px;height:230px;background:linear-gradient(120deg,#d6dadc,#a9b0b4 60%,#6f777c)"></div>

<div class="divider" style="top:2030px"></div>

<div class="photo" role="img" aria-label="Laboratory microscope and sample tubes" style="left:40px;top:2080px;width:380px;height:250px;background:linear-gradient(135deg,#dfe4e7,#b8c2c8 60%,#8a969d)"></div>
<h2 class="stitle" style="left:460px;top:2085px">Laboratory Services</h2>
<p class="abs" style="left:460px;top:2145px;width:700px">Contrary to popular belief, Lorem Ipsum is not simply random text. It has roots in a piece of classical Latin literature from 45 BC, making it over 2000 years old. A professor at a college in Virginia looked up one of the more obscure Latin words from a passage, and going through the cites of the word in classical literature, discovered the undoubtable source. The passage comes from a treatise on the theory of ethics, very popular during the Renaissance. The first line comes from a line in that same section.</p>

<section class="appt" role="img" aria-label="Smiling doctor in a white coat holding a clipboard in a clinic room">
  <div class="form-box">
    <h2>Request an Appointment</h2>
    <p class="sub">There are many variations</p>
    <div class="fields">
      <div class="field">Please Select One <span>&#9662;</span></div>
      <div class="field">Name</div>
      <div class="field">Email</div>
      <div class="field">Phone</div>
      <div class="field">Service</div>
      <div class="field">Proposed Date</div>
      <div class="field">Proposed Time</div>
      <div class="btn-blue">REQUEST AN APPOINTMENT</div>
    </div>
  </div>
</section>

<h2 class="blog-title">Blog</h2>

<div class="photo" role="img" aria-label="Clinic signboard outside the building" style="left:40px;top:2960px;width:240px;height:150px;background:linear-gradient(135deg,#dfe6ea,#b7c4cc)"></div>
<div class="post" style="left:300px;top:2960px;width:440px">
  <h4>Test of perspiciatis unde omnis</h4>
  <div class="meta">Feb 8, 2017 by Ada Okoro</div>
  <p>Please enter excerpt text and this short excerpt goes here to summarise the post. Nemo enim ipsam voluptatem quia voluptas sit aspernatur aut odit aut fugit, sed quia consequuntur magni dolores eos qui ratione sequi nesciunt.</p>
</div>
<div class="photo" role="img" aria-label="Eye test instrument in a consulting room" style="left:780px;top:2960px;width:380px;height:150px;background:linear-gradient(135deg,#cfd6da,#8f9ba2)"></div>

<div class="photo" role="img" aria-label="Front view of the clinic building" style="left:40px;top:3130px;width:240px;height:120px;background:linear-gradient(135deg,#e3e7ea,#a5b1b8)"></div>
<div class="post" style="left:300px;top:3130px;width:440px">
  <h4>Lorem ipsum dolor</h4>
  <div class="meta">Feb 8, 2017 by Ada Okoro</div>
  <p>Nemo enim ipsam voluptatem quia voluptas sit aspernatur aut odit aut fugit, sed quia consequuntur magni dolores eos qui ratione sequi.</p>
</div>
<div class="post" style="left:780px;top:3130px;width:220px">
  <h4>At vero eos et accusamus</h4>
  <div class="meta">Feb 8, 2017 by Ada Okoro</div>
  <p>Et harum quidem rerum facilis est et expedita distinctio libero tempore.</p>
</div>
<div class="photo" role="img" aria-label="Optical test equipment on a desk" style="left:1020px;top:3130px;width:140px;height:120px;background:linear-gradient(135deg,#d9dfe2,#9aa6ad)"></div>

<footer class="footer">
  <div class="fcol" style="left:40px;width:340px">
    <h4>ABOUT VORANTACARE</h4>
    <div class="row"><svg width="14" height="14" viewBox="0 0 24 24"><path fill="#1e9ad6" d="M12 2a7 7 0 0 0-7 7c0 5 7 13 7 13s7-8 7-13a7 7 0 0 0-7-7zm0 9.5a2.5 2.5 0 1 1 0-5 2.5 2.5 0 0 1 0 5z"/></svg><span>21 Harbour Crest Road, Lekki Phase 1,<br>Lagos, Nigeria</span></div>
    <div class="row"><svg width="14" height="14" viewBox="0 0 24 24"><path fill="#1e9ad6" d="M6.6 10.8a15 15 0 0 0 6.6 6.6l2.2-2.2c.3-.3.7-.4 1-.2 1.1.4 2.3.6 3.6.6.6 0 1 .4 1 1V20c0 .6-.4 1-1 1A17 17 0 0 1 3 4c0-.6.4-1 1-1h3.5c.6 0 1 .4 1 1 0 1.3.2 2.5.6 3.6.1.3 0 .7-.2 1z"/></svg><span>+234 800 555 0142</span></div>
    <div class="row"><svg width="14" height="14" viewBox="0 0 24 24"><rect x="2" y="5" width="20" height="14" fill="#1e9ad6"/><path d="M2 5l10 8 10-8" fill="none" stroke="#2a2e33" stroke-width="1.5"/></svg><span>hello@vorantacare.com</span></div>
  </div>
  <div class="fcol" style="left:520px">
    <h4>LINKS</h4>
    <ul class="links"><li>Home</li><li>Dental Services</li><li>Eye Services</li><li>Appointment</li><li>Blog</li><li>Careers</li><li>Contact Us</li><li>Staff</li></ul>
  </div>
  <div class="fcol" style="left:800px">
    <h4>ENQUIRY FORM</h4>
    <div class="finput">Name</div>
    <div class="finput">Email</div>
    <div class="finput tall">Message</div>
    <span class="fbtn">SUBMIT</span>
  </div>
</footer>
<div class="bottombar"><span>Vorantacare © 2017. All Rights Reserved.</span><span>Top &#9650;</span></div>

</body>
</html>
```